IT Company Business Card Design w/Stationary Design

We have a great logo we like! We are looking to redesign our business cards and all company logo'd merchandise/materials.

We are an IT Company located near the Bay Area (San Francisco, CA). We specialize in Managed Services and offer complete IT Computer and Network Support to Businesses of all sizes. We thrive on making a lasting impression. We have been doing IT for 15yrs+ but are young at heart. We like to stand out and be different. We want to be unique and have a recognizable brand. We need our logo to represent who we are. We are young, professional, creative and outstanding. We don't want to blend in, we want to stand out. Our business card needs to stand out and grab attention. Something Bold, yet simple and clean. (I will provide ideas of what we like to give a taste of what we are looking for).

The design can include any kind of texture/artistic design or sizing EXCEPT please "no square card designs" as they don't seem to fit in wallets very well. We dont mind curved edges, rounded corners, vertical layouts or horizontal layouts, embossing, letter press or raised surfaces. Again, we dont want to look average or plain or boring. :) Be creative - yet practical! We have ordered from Pebblecraft designs before and been very happy. Their card sizes tend to be a little different, so beware. Hope this helps!

Target Market(s)

Businesses - Small to Medium, Corporations, Publicly Traded Companies

Industry/Entity Type

Business

Contact Information for Business Card

Harbor Lantern IT
7318 Quillby Avenue
Suite F
Modesto, CA 95871

Office 209.555.0137
Direct 209.555.0182
Cell 209.555.0164

Ross Tavener
Founder, CEO
www.hlit-example.com
rtavener@hlit-example.com

Locations Serviced: Modesto, Stockton, Pleasanton, Fresno (incorporate this on the card ONLY if there's a good place to do so).

What we specialize in: Computer, Network, Voice, Data. (IT Services)

Our Logo Colors: Black and Blue (#006699). Open to using grey or orange as well - but not required. Don't want too busy....

Logo Font: "Cinthe" (Will attach logo font). We want type style to be clean. You can show different font types including our logo font - and we are open to other font ideas.

The logo can be separated. You can use elements together or apart. Surprise us! :) We "REALLY" want the "hl" to be our identifier/our brand people recognize.

Font styles to use
Sans Serif

Colors
0355a3
3176b5
f37122
f78f20
faa54b
474747
aaaaaa
757575
000000

Requirements
Must have
• Bold, Big, Colorful, Modern/yet Fun, Clean Design, Stand Out Presence, Texture would be welcomed - but not necessary, Card design shape can include cut corners or rounded or square edges. Be creative. (HOWEVER, we don't want a square design because we have found it doesn't fit in wallets that easily).
• We do like using Pebblecraft printing company (Which they have particular sizing on their card templates - beware), but are open to other design templates/printing companies as well. We just want to make sure its easy to find a print company to do our work. Too unique could be costly and hard to get cards printed.
• Colors to use: Our logo Blue (#006699), with either whites, grays, black, shades of our blue, and maybe a pinch of orange if needed. Primarily, blue, white, gray or black.
Nice to have
• Texture would be cool or little different edging or shape - but nothing too costly to print. I have seen cards with 3 sharp edges and one round edge. Something like that would be cool as an option. Or a vertical card.
• I love a faded watermark look. It would be nice to see some shading of our circle logo on a few designs. The circle with "hl" in it OR.... taking just the "hl" and using it alone.
Should not have
• No square card designs. Nothing too expensive or elaborate to print. No busy fonts. Do not like Times New Roman type fonts (too old looking). Not a lot of orange (if you even choose to use some orange).

```html
<!DOCTYPE html>
<html lang="en">
<head>
<meta charset="utf-8">
<title>Harbor Lantern IT – Business Card</title>
<link rel="stylesheet" href="https://fonts.googleapis.com/css2?family=Questrial&display=swap">
<style>
  :root {
    --backdrop: #8c8c8c;
    --card-white: #f7f7f7;
    --brand-blue: #1390cf;
    --brand-blue-deep: #0f6fae;
    --brand-blue-light: #1aa3dc;
    --ink: #3a3a3a;
    --ink-soft: #7a7a7a;
    --white: #ffffff;
  }
  * { margin: 0; padding: 0; box-sizing: border-box; }
  html, body {
    width: 1200px;
    height: 900px;
    overflow: hidden;
    background: var(--backdrop);
    font-family: "Questrial", sans-serif;
  }
  .canvas {
    width: 1200px;
    height: 900px;
    display: flex;
    flex-direction: column;
    align-items: center;
    justify-content: center;
    gap: 60px;
  }
  .card {
    width: 620px;
    height: 354px;
    border-radius: 18px;
    position: relative;
    overflow: hidden;
    box-shadow: 0 6px 18px rgba(0,0,0,0.25);
  }

  /* Front */
  .card-front { background: var(--card-white); }
  .contact {
    position: absolute;
    left: 38px;
    top: 30px;
    color: var(--ink);
    font-size: 17px;
    line-height: 1.22;
  }
  .contact-name {
    color: var(--brand-blue);
    font-size: 25px;
    letter-spacing: 1px;
  }
  .contact-title {
    color: var(--ink-soft);
    font-size: 18px;
    letter-spacing: 1px;
    margin-bottom: 12px;
  }
  .contact-block { margin-bottom: 6px; }
  .contact-lines { list-style: none; margin-top: 6px; }
  .contact-lines li {
    display: flex;
    align-items: center;
    gap: 8px;
    height: 24px;
  }
  .contact-lines svg { width: 15px; height: 15px; fill: var(--brand-blue-deep); flex: none; }
  .brand-mark {
    position: absolute;
    right: 50px;
    top: 40px;
    width: 210px;
    display: flex;
    flex-direction: column;
    align-items: center;
    gap: 16px;
  }
  .brand-circle {
    width: 210px;
    height: 210px;
    border-radius: 50%;
    background: radial-gradient(circle at 35% 30%, var(--brand-blue-light), var(--brand-blue-deep));
  }
  .brand-name {
    color: var(--brand-blue);
    font-size: 26px;
    letter-spacing: 1px;
    white-space: nowrap;
  }

  /* Back */
  .card-back {
    background: linear-gradient(135deg, var(--brand-blue-light) 0%, var(--brand-blue) 45%, var(--brand-blue-deep) 100%);
    color: var(--white);
    display: flex;
    flex-direction: column;
    align-items: center;
    justify-content: center;
    text-align: center;
  }
  .back-dot {
    width: 58px;
    height: 58px;
    border-radius: 50%;
    background: var(--white);
    margin-bottom: 14px;
  }
  .back-name {
    font-size: 44px;
    letter-spacing: 2px;
    line-height: 1;
    margin-bottom: 30px;
  }
  .specialty {
    font-size: 19px;
    line-height: 1.3;
    letter-spacing: 0.5px;
  }
</style>
</head>
<body>
<main class="canvas">

  <section class="card card-front" aria-label="Business card front">
    <div class="contact">
      <p class="contact-name">Ross Tavener</p>
      <p class="contact-title">Founder, CEO</p>
      <div class="contact-block">
        <p>Harbor Lantern IT</p>
        <p>7318 Quillby Avenue</p>
        <p>Suite F Modesto, CA 95871</p>
      </div>
      <div class="contact-block">
        <p>Locations Serviced :</p>
        <p>Modesto, Stockton</p>
        <p>Pleasanton, Fresno</p>
      </div>
      <ul class="contact-lines">
        <li>
          <svg viewBox="0 0 16 16" aria-hidden="true"><path d="M1 5c0-2 3-3 7-3s7 1 7 3v1h-4V5H5v1H1z"/><rect x="3" y="7" width="10" height="7" rx="1.5"/></svg>
          209.555.0137
        </li>
        <li>
          <svg viewBox="0 0 16 16" aria-hidden="true"><path d="M4 1l2.5 3-1.5 2c1 2 3 4 5 5l2-1.5 3 2.5-2 2.5C7 14 2 9 1.5 3.5z"/></svg>
          209.555.0182
        </li>
        <li>
          <svg viewBox="0 0 16 16" aria-hidden="true"><path d="M4.5 0h7A1.5 1.5 0 0 1 13 1.5v13a1.5 1.5 0 0 1-1.5 1.5h-7A1.5 1.5 0 0 1 3 14.5v-13A1.5 1.5 0 0 1 4.5 0zM5 2v10h6V2zm3 11a1 1 0 1 0 0 2 1 1 0 0 0 0-2z"/></svg>
          209.555.0164
        </li>
        <li>
          <svg viewBox="0 0 16 16" aria-hidden="true"><path d="M1 3h14v1L8 9 1 4z"/><path d="M1 5.5l7 5 7-5V13H1z"/></svg>
          rtavener@hlit-example.com
        </li>
      </ul>
    </div>
    <div class="brand-mark">
      <div class="brand-circle"></div>
      <p class="brand-name">Harbor Lantern</p>
    </div>
  </section>

  <section class="card card-back" aria-label="Business card back">
    <div class="back-dot"></div>
    <p class="back-name">Harbor Lantern</p>
    <p class="specialty">We Specialize in:<br>Computer, Network, Voice, Data. (IT Services)</p>
  </section>

</main>
</body>
</html>
```